11th Annual Vemtora Forum Flyer - Save the Date

We need a flyer for our annual Forum that will be creative with the theme of the Forum while highlighting our conference Title and Topics. Flyer should allow for a header that can be used consistently across conference communication. This is our 11th Annual Forum, which will take place outside of Houston, Texas at Bel Costano Resort and Spa.

Target Market(s)

Architects, engineers, contractors, universities, building project Owners

Industry/Entity Type

Construction

Font styles to use
Sans Serif

Colors

Designer to choose colors to be used in the design.

Requirements
Must have
• Title, date, location, key topics (title only), logo. See attached for breakdown of information.
Nice to have
• Creativity with the theme of the Forum, ability to slice flyer so that a portion can be used for a header in other conference documents.
• Mention of Closing Keynote, Dale Hutton
Should not have
• Please don't use the topic descriptions in the Flyer. Just the main titles of the topics is necessary.
• Should not be too word, but eye-catching with graphics and main

```html
<!DOCTYPE html>
<html lang="en">
<head>
<meta charset="utf-8">
<title>Vemtora Forum 2019 – Save the Date</title>
<link href="https://fonts.googleapis.com/css2?family=Montserrat:wght@400;600;700;800&display=swap" rel="stylesheet">
<style>
  :root{
    --navy:#1c3a74;
    --blue:#2a5fae;
    --sky:#cfe3f4;
    --sky-deep:#9cc4e6;
    --green:#7cc242;
    --green-dark:#4f9a2a;
    --grey:#c9ccd1;
    --grey-dark:#8d939b;
    --white:#ffffff;
  }
  html,body{margin:0;padding:0;overflow:hidden;background:#fff;}
  .flyer{
    position:relative;width:849px;height:1200px;overflow:hidden;
    background:var(--white);font-family:'Montserrat',sans-serif;color:var(--navy);
  }
  .abs{position:absolute;}

  /* imagery */
  .photo-tower{
    left:420px;top:-240px;width:700px;height:700px;border-radius:50%;
    background:linear-gradient(135deg,#3d7f5e 0%,#6fae8a 30%,#2f6f6a 55%,#9fd1c0 80%,#dff1ea 100%);
    box-shadow:0 0 0 14px var(--green),0 0 0 24px var(--white),0 0 0 30px var(--sky-deep);
  }
  .photo-facade{
    left:300px;top:470px;width:549px;height:730px;
    background:linear-gradient(160deg,#eef0f2 0%,var(--grey) 40%,#a9aeb5 70%,#dfe2e5 100%);
  }
  .photo-site{
    left:-60px;top:760px;width:460px;height:460px;border-radius:50%;
    background:linear-gradient(180deg,#e8f1f8 0%,#b9d2e6 45%,#7b8fa3 75%,#4e5b66 100%);
    box-shadow:0 0 0 12px var(--green),0 0 0 22px var(--white),0 0 0 28px var(--sky-deep);
  }

  /* header */
  .brand{left:60px;top:30px;width:250px;text-align:center;}
  .brand-mark{width:70px;height:70px;border-radius:50%;background:var(--blue);margin:0 auto 10px;}
  .brand-name{font-size:30px;font-weight:800;color:var(--navy);letter-spacing:1px;}
  .brand-tag{font-size:11px;font-weight:600;color:var(--navy);margin-top:4px;}

  .event-title{left:85px;top:222px;margin:0;font-size:48px;font-weight:800;line-height:1.1;color:var(--navy);}

  .theme-tab{
    left:14px;top:335px;padding:6px 24px;background:var(--green);color:var(--white);
    font-size:26px;font-weight:800;letter-spacing:1px;border-radius:0 24px 24px 0;
  }
  .theme-band{
    left:0;top:383px;width:520px;height:92px;padding-left:40px;box-sizing:border-box;
    background:linear-gradient(90deg,var(--sky) 0%,#e9f2fa 100%);
    display:flex;flex-direction:column;justify-content:center;
    font-size:27px;font-weight:800;line-height:1.25;color:var(--navy);
    border-bottom:6px solid var(--green);
  }

  /* keynote */
  .keynote{
    left:560px;top:380px;width:290px;height:290px;border-radius:50%;background:var(--green);
  }
  .keynote-inner{
    position:absolute;left:50px;top:50px;width:190px;height:190px;border-radius:50%;
    background:var(--sky);border:8px solid var(--white);box-sizing:border-box;
    display:flex;align-items:center;justify-content:center;text-align:center;
    font-size:40px;font-weight:800;line-height:1.05;color:var(--navy);
  }
  .keynote-label{
    position:absolute;left:6px;top:70px;font-size:22px;font-weight:700;color:var(--white);
    writing-mode:vertical-rl;transform:rotate(180deg);letter-spacing:1px;
  }

  /* venue */
  .venue{
    left:-20px;top:560px;width:290px;height:290px;border-radius:50%;
    background:var(--sky);border:10px solid var(--white);box-sizing:border-box;
    box-shadow:0 0 0 6px var(--sky-deep);
    display:flex;flex-direction:column;align-items:center;justify-content:center;
    text-align:center;padding:0 20px 0 40px;
  }
  .venue-name{font-size:27px;font-weight:800;line-height:1.2;color:var(--navy);margin-top:8px;}

  /* topics */
  .topics-tab{
    left:523px;top:798px;width:170px;height:42px;background:var(--green);color:var(--white);
    font-size:24px;font-weight:800;display:flex;align-items:center;justify-content:center;
    border-radius:21px 21px 0 0;
  }
  .topics-list{
    left:396px;top:845px;width:453px;margin:0;padding:14px 0 14px 30px;box-sizing:border-box;
    background:var(--blue);color:var(--white);list-style:none;
    font-size:21px;font-weight:600;line-height:1.55;
  }
  .event-date{
    left:424px;top:1000px;padding:8px 26px;background:var(--white);
    font-size:26px;font-weight:800;color:var(--navy);border-bottom:6px solid var(--green);
  }
</style>
</head>
<body>
<div class="flyer">
  <div class="abs photo-tower" role="img" aria-label="Glass office tower rising against the sky"></div>
  <div class="abs photo-facade" role="img" aria-label="Grey modern building facade seen from below"></div>
  <div class="abs photo-site" role="img" aria-label="Construction site with cranes and steel frame"></div>

  <header class="abs brand">
    <div class="brand-mark"></div>
    <div class="brand-name">Vemtora</div>
    <div class="brand-tag">Leadership in Building Projects Network</div>
  </header>

  <h1 class="abs event-title">Vemtora FORUM<br>2019</h1>

  <div class="abs theme-tab">THEME</div>
  <div class="abs theme-band">
    <span>THE THREE-LEGGED STOOL</span>
    <span>BALANCED OR BROKEN?</span>
  </div>

  <div class="abs keynote">
    <span class="keynote-label">Closing Keynote</span>
    <div class="keynote-inner">Dale<br>Hutton</div>
  </div>

  <div class="abs venue">
    <svg width="34" height="44" viewBox="0 0 34 44" aria-hidden="true">
      <path d="M17 2C9 2 3 8 3 16c0 11 14 26 14 26s14-15 14-26C31 8 25 2 17 2z" fill="var(--blue)"/>
      <circle cx="17" cy="16" r="6" fill="var(--white)"/>
    </svg>
    <div class="venue-name">Bel Costano Resort and Spa, Texas</div>
  </div>

  <div class="abs topics-tab">TOPICS</div>
  <ol class="abs topics-list">
    <li>1. The Right Contract Management</li>
    <li>2. The Right Culture</li>
    <li>3. The Right Subcontractors</li>
  </ol>

  <div class="abs event-date">Date: dd, month, 2019</div>
</div>
</body>
</html>
```